Communication and Marketing agency needs a new presentation card

We are a group of communication and marketing agencies specialized in companies that are in the logistics and industrial sector. The head agency is TELVANO Grupo and the group consists of 4 agencies: TELVANO Media, TELVANO Digital, TELVANO Research and EnlazaPorImagen. We hace 4 offices in Spain (Madrid, Barcelona, Valencia and Murcia). We are looking for a clean and attractive design that transmits our experience, brand presence in the market and knowledge to those who receive the card.It has to maintain the colors of the logo that is attached.
Target Market(s)
logistics and industrial sector
Marketing department
Clean and attractive design

```html
<!DOCTYPE html>
<html lang="en">
<head>
<meta charset="utf-8">
<title>TELVANO Digital – Business Card</title>
<link href="https://fonts.googleapis.com/css2?family=Open+Sans:wght@300;400;700&display=swap" rel="stylesheet">
<style>
  :root {
    --bg: #e9e9ea;
    --card: #ffffff;
    --red: #c0213a;
    --red-dark: #a51f24;
    --grey-band: #4d4a49;
    --grey-logo: #5a5a5c;
    --ink: #1f1f22;
    --faint-pink: #fbeff0;
    --faint-grey: #f3f3f4;
  }
  * { margin: 0; padding: 0; box-sizing: border-box; }
  html, body { width: 1200px; height: 960px; overflow: hidden; }
  body {
    background: var(--bg);
    font-family: "Open Sans", Arial, sans-serif;
    position: relative;
  }
  .card {
    position: absolute;
    left: 240px;
    width: 720px;
    height: 412px;
    background: var(--card);
    overflow: hidden;
    box-shadow: 0 6px 18px rgba(0,0,0,0.12);
  }
  .card--back { top: 44px; }
  .card--front { top: 504px; }
  .stripes { position: absolute; left: 0; top: 0; }

  .brand {
    position: absolute;
    display: flex;
    align-items: center;
    gap: 12px;
    color: var(--grey-logo);
    font-weight: 300;
    letter-spacing: 3px;
    white-space: nowrap;
  }
  .brand__mark {
    width: 14px; height: 14px;
    background: var(--red);
  }
  .card--back .brand { left: 210px; top: 160px; font-size: 46px; }
  .card--front .brand { right: 40px; top: 44px; font-size: 36px; }

  .band {
    position: absolute;
    left: 0; right: 0; bottom: 0;
    background: var(--grey-band);
  }
  .card--back .band { height: 54px; }
  .card--front .band { height: 40px; }
  .band__accent {
    position: absolute;
    right: 0; top: 0; bottom: 0;
    background: var(--red);
    border-left: 4px solid var(--card);
  }
  .card--back .band__accent { width: 92px; }
  .card--front .band__accent { width: 150px; }
  .band__url {
    position: absolute;
    left: 190px; top: 50%;
    transform: translateY(-50%);
    color: var(--red);
    font-weight: 700;
    font-size: 15px;
    letter-spacing: 2px;
  }

  .divider {
    position: absolute;
    left: 190px; right: 40px;
    top: 258px;
    height: 3px;
    background: var(--red);
  }
  .person {
    position: absolute;
    left: 190px; top: 196px;
    color: var(--red);
  }
  .person__name { font-weight: 700; font-size: 27px; line-height: 1.05; letter-spacing: 0.5px; }
  .person__role { font-weight: 400; font-size: 17px; line-height: 1.3; }
  .contact {
    position: absolute;
    left: 190px; top: 270px;
    list-style: none;
    color: var(--ink);
    font-size: 19px;
    line-height: 1.3;
  }
  .address {
    position: absolute;
    right: 40px; top: 272px;
    text-align: right;
    color: var(--ink);
    font-size: 15px;
    line-height: 1.4;
    font-style: normal;
  }
</style>
</head>
<body>

<section class="card card--back" aria-label="Card back">
  <svg class="stripes" width="720" height="412" viewBox="0 0 720 412" aria-hidden="true">
    <polygon points="0,60 180,60 40,412 0,412" fill="var(--faint-grey)"/>
    <polygon points="200,60 260,60 120,412 60,412" fill="var(--faint-pink)"/>
    <polygon points="285,60 320,60 180,412 145,412" fill="var(--faint-pink)"/>
    <rect x="0" y="0" width="720" height="60" fill="var(--card)"/>
  </svg>
  <div class="brand"><span class="brand__mark"></span>TELVANO Digital</div>
  <div class="band">
    <span class="band__url">WWW.TELVANODIGITAL.COM</span>
    <span class="band__accent"></span>
  </div>
</section>

<section class="card card--front" aria-label="Card front">
  <svg class="stripes" width="200" height="412" viewBox="0 0 200 412" aria-hidden="true">
    <polygon points="30,0 48,0 0,107 0,67" fill="var(--grey-band)"/>
    <polygon points="62,0 112,0 0,250 0,140" fill="var(--red)"/>
    <polygon points="130,0 195,0 11,412 0,412 0,290" fill="var(--red-dark)"/>
  </svg>
  <div class="brand"><span class="brand__mark"></span>TELVANO Digital</div>

  <div class="person">
    <p class="person__name">MARCUS DELVANE</p>
    <p class="person__role">Managing Director</p>
  </div>
  <div class="divider"></div>
  <ul class="contact">
    <li>555.014.2187</li>
    <li>555.014.2120</li>
    <li>hola@telvanodigital.es</li>
  </ul>
  <address class="address">
    2410 Harbor Line Ave<br>
    Valemont, LA 70190<br>
    www.telvanodigital.com
  </address>

  <div class="band"><span class="band__accent"></span></div>
</section>

</body>
</html>
```